2 Flyers of Company Core Values/Mission Statement & Who We Are

We are a construction company that needs two flyers for our core values/mission statement and Who We Are. We want something unique and a little edgy.

Flyer 1 will consist of our core values and mission statement below (chart or graphics style would be good). We don't want just wording.

I. Core Values
a. Respect for all people
b. Open, honest, proactive, and energetic two-way communication
c. Our word is our promise
d. Invest in our team members to provide them opportunities for development and advancement
e. Foster an atmosphere that encourages innovation and continuous improvement
f. Sustain a safety-focused culture

J. Core Value Statement
Mission Statement: Corvane Construction is an ever-advancing Christian principled company guided by the core values of respect, proactive two-way communication, keeping promises, investing in people, and innovation. Accordingly, we are committed to excellence in everything we do.

Flyer 2 will consists of a page of "Who We Are" to contain the following information:

A. Strengths/Core Competencies
a. Loyal to employees
b. Honest and fair with employees and customers
c. High-quality work
d. Adaptable to changing market conditions
e. Employees: talented workers, superintendents, and project managers
f. Embrace and adapt to changing technology
B. Mindshare (words we own)
a. Difficult projects (in each sector we serve)
C. What (Product & Service)
a. Timely and successful construction project completion
D. Brand Promise
a. 90% of our customers would do business with us again
b. We treat each customer's project like it was our own investment
E. Brand Promise Guarantee
a. We are a Christian principled company and never compromise our integrity. We are committed to excellence in everything we do.
F. One Phase Strategy (Key to making Money)
a. Understand the markets we serve and manage our people to efficiently serve the customer
G. Differentiating Factors
a. Access to a flexible source of high-quality, on-demand labor
b. More professional than small competitors
c. Big enough to handle the most difficult tasks but small enough to have a personal relationship with the customer
d. Zero-item punch list at project completion
H. X-Factor
a. Access to a flexible source of high-quality, dedicated & talented labor force not available to competitors
J. Purpose
a. Our goal is to improve the quality of life in the communities we serve through constructing great and successful projects.

Industry/Entity Type

Construction

```html
<!DOCTYPE html>
<html lang="en">
<head>
<meta charset="utf-8">
<title>Corvane Construction – Core Values</title>
<link href="https://fonts.googleapis.com/css2?family=Open+Sans:wght@300;400&display=swap" rel="stylesheet">
<style>
  :root {
    --navy: #22445f;
    --white: #ffffff;
    --text-soft: #e9eef3;
    --brand-blue: #3a8fd0;
    --sky-top: #c3cde0;
    --sky-mid: #7f90b6;
    --dusk: #8a7a9e;
    --city-glow: #6b5470;
    --city-dark: #2a2838;
    --city-amber: #b07a3a;
  }
  * { margin: 0; padding: 0; box-sizing: border-box; }
  html, body {
    width: 1200px;
    height: 874px;
    overflow: hidden;
    background: var(--navy);
    font-family: "Open Sans", Arial, sans-serif;
  }
  .flyer {
    position: relative;
    width: 1200px;
    height: 874px;
    background: var(--navy);
    color: var(--white);
  }
  .city-photo {
    position: absolute;
    left: 0; top: 0;
    width: 538px;
    height: 874px;
    background:
      radial-gradient(ellipse 75% 22% at 50% 68%, rgba(176,122,58,0.55), transparent 70%),
      linear-gradient(180deg,
        var(--sky-top) 0%,
        var(--sky-mid) 22%,
        var(--dusk) 40%,
        var(--city-glow) 50%,
        var(--city-dark) 66%,
        #3a2f35 85%,
        var(--city-dark) 100%);
  }
  .brand {
    position: absolute;
    left: 65px;
    top: 54px;
    display: flex;
    align-items: center;
    gap: 14px;
  }
  .brand-dot {
    width: 80px;
    height: 80px;
    border-radius: 50%;
    background: var(--brand-blue);
    flex: none;
  }
  .brand-name {
    color: var(--white);
    font-weight: 400;
    font-size: 20px;
  }
  .values-title {
    position: absolute;
    left: 611px;
    top: 109px;
    font-weight: 300;
    font-size: 51px;
    line-height: 61px;
  }
  .mission-statement {
    position: absolute;
    left: 611px;
    top: 206px;
    width: 560px;
    font-weight: 300;
    font-size: 25.5px;
    line-height: 35.2px;
    color: var(--text-soft);
    white-space: nowrap;
  }
  .value-card {
    position: absolute;
    display: flex;
    align-items: center;
    justify-content: center;
    text-align: center;
    border: 1.5px solid var(--white);
    border-radius: 16px;
    padding: 0 10px;
    font-weight: 400;
    font-size: 18.5px;
    line-height: 22.7px;
    white-space: nowrap;
  }
  .card-communication { left: 588px; top: 486px; width: 258px; height: 101px; }
  .card-innovation    { left: 871px; top: 486px; width: 276px; height: 101px; }
  .card-respect       { left: 588px; top: 605px; width: 172px; height: 86px; }
  .card-promise       { left: 780px; top: 605px; width: 173px; height: 86px; }
  .card-safety        { left: 973px; top: 605px; width: 173px; height: 86px; }
  .card-team          { left: 588px; top: 715px; width: 558px; height: 85px; }
</style>
</head>
<body>
  <main class="flyer">
    <div class="city-photo" role="img" aria-label="Aerial photo of a city skyline at dusk with glowing lights and network connection lines"></div>
    <div class="brand">
      <span class="brand-dot"></span>
      <span class="brand-name">Corvane Construction</span>
    </div>

    <h1 class="values-title">Core Values</h1>
    <p class="mission-statement">Corvane Construction is an ever-advancing<br>Christian principled company guided by the<br>core values of respect, proactive two-way<br>communication, keeping promises, investing<br>in people, and innovation. Accordingly, we are<br>committed to excellence in everything we do.</p>

    <div class="value-card card-communication">Open, honest, proactive,<br>and energetic two-way<br>communication</div>
    <div class="value-card card-innovation">Foster an atmosphere that<br>encourages innovation and<br>continuous improvement</div>
    <div class="value-card card-respect">Respect for all<br>people</div>
    <div class="value-card card-promise">Our word is our<br>promise</div>
    <div class="value-card card-safety">Sustain a safety-<br>focused culture</div>
    <div class="value-card card-team">Invest in our team members to provide them<br>opportunities for development and advancement</div>
  </main>
</body>
</html>
```